Letterbox drop flyers for local business

I need a flyer design for my small business located in Canberra ACT called "Tallowbend Garden Care" My company is a landscaping business offering garden design, landscaping services, garden maintenance and horticultural services. I would like to have a flyer I can leave at nurseries and do letterbox drops with that highlight the professional quality of our services and also our brand feel of rural Australia and old fashioned vibe. The flyer should highlight our services and our "free quote" policy. Attached is my business logo.

Industry/Entity Type

Small Business

Font styles to use
Serif
Decorative

Colors
f37122
fcca95
ec1f27
abd036
9bcb3c

Requirements
Must have
• A list of our services and all my contact information as well as our offer for free quotes. Present this flyer and customer receives first hour of gardening free
Nice to have
• I would like the overall feel of the design to be old fashioned. Think old painted advertisments for wickam soap and brennicks biscuits, or an old dorvan pick-up truck with the dog in the back, want to highlight our quality but also give my customers a feel for our brand as a whole

```html
<!DOCTYPE html>
<html lang="en">
<head>
<meta charset="utf-8">
<title>Tallowbend Garden Care – Flyer Cards</title>
<link href="https://fonts.googleapis.com/css2?family=Didact+Gothic&display=swap" rel="stylesheet">
<style>
  :root {
    --backdrop: #c88d55;
    --card: #1f1a10;
    --card-edge: #0f0c06;
    --panel-light: #f3cf6e;
    --panel-mid: #e6b44e;
    --panel-dark: #c9923a;
    --brand-red: #8a1f1c;
    --tan: #e2c27a;
    --leaf: #4f7d2c;
    --rule: #cfae63;
  }
  * { margin: 0; padding: 0; box-sizing: border-box; }
  html, body { width: 1200px; height: 867px; overflow: hidden; }
  body {
    background: var(--backdrop);
    font-family: "Didact Gothic", "Century Gothic", sans-serif;
    position: relative;
  }
  .card {
    position: absolute;
    top: 135px;
    width: 420px;
    height: 595px;
    background: var(--card);
    border: 2px solid var(--card-edge);
    box-shadow: 0 6px 14px rgba(0,0,0,.35);
  }
  .card--contact { left: 165px; }
  .card--services { left: 615px; }

  .brand-panel {
    position: absolute;
    left: 10px; top: 15px;
    width: 397px; height: 295px;
    background: radial-gradient(ellipse at 50% 45%, var(--panel-light) 0%, var(--panel-mid) 60%, var(--panel-dark) 100%);
    box-shadow: 0 3px 8px rgba(0,0,0,.5);
  }
  .brand-name {
    position: absolute;
    inset: 0;
    display: flex;
    flex-direction: column;
    align-items: center;
    justify-content: center;
    color: var(--brand-red);
    text-align: center;
    line-height: 1.05;
  }
  .brand-name__main { font-size: 58px; }
  .brand-name__sub { font-size: 34px; margin-top: 10px; }

  .centered {
    position: absolute;
    left: 0; width: 100%;
    text-align: center;
    white-space: nowrap;
  }
  .contact-name { top: 378px; font-size: 24px; color: var(--tan); letter-spacing: .5px; }
  .contact-phone { top: 428px; font-size: 54px; color: var(--leaf); letter-spacing: 1px; }
  .contact-abn { top: 493px; font-size: 15px; color: var(--leaf); letter-spacing: 7px; }
  .contact-web { top: 521px; font-size: 18px; color: var(--leaf); }
  .hr {
    position: absolute;
    left: 45px; width: 330px; height: 1px;
    background: var(--rule);
  }

  .services-heading { top: 326px; font-size: 23px; color: var(--tan); letter-spacing: .5px; }
  .service-list { list-style: none; }
  .service { font-size: 22px; color: var(--leaf); letter-spacing: .5px; }
  .rule-dotted {
    position: absolute;
    left: 45px; width: 330px; height: 8px;
  }
  .offer {
    top: 486px;
    font-size: 34px;
    line-height: 35px;
    color: var(--tan);
  }
  .bonus {
    top: 560px;
    font-size: 14px;
    color: var(--leaf);
    letter-spacing: .5px;
  }
</style>
</head>
<body>

<section class="card card--contact" aria-label="Contact card">
  <div class="brand-panel" role="img" aria-label="Warm golden panel with faint scroll ornaments behind the business name">
    <div class="brand-name">
      <span class="brand-name__main">Tallowbend</span>
      <span class="brand-name__sub">Garden Care</span>
    </div>
  </div>
  <p class="centered contact-name">MARISOL QUENNELL</p>
  <p class="centered contact-phone">0400582917</p>
  <div class="hr" style="top:489px"></div>
  <p class="centered contact-abn">ABN: 62 305 718 449</p>
  <div class="hr" style="top:514px"></div>
  <p class="centered contact-web">tallowbendgardensact.com.au</p>
</section>

<section class="card card--services" aria-label="Services card">
  <div class="brand-panel" role="img" aria-label="Warm golden panel with faint scroll ornaments behind the business name">
    <div class="brand-name">
      <span class="brand-name__main">Tallowbend</span>
      <span class="brand-name__sub">Garden Care</span>
    </div>
  </div>
  <p class="centered services-heading">SPECIALISING IN</p>

  <svg class="rule-dotted" style="top:352px" viewBox="0 0 330 8"><line x1="4" y1="4" x2="326" y2="4" stroke="#cfae63" stroke-width="1.5"/><circle cx="4" cy="4" r="3" fill="#cfae63"/><circle cx="326" cy="4" r="3" fill="#cfae63"/></svg>
  <svg class="rule-dotted" style="top:384px" viewBox="0 0 330 8"><line x1="4" y1="4" x2="326" y2="4" stroke="#cfae63" stroke-width="1.5"/><circle cx="4" cy="4" r="3" fill="#cfae63"/><circle cx="326" cy="4" r="3" fill="#cfae63"/></svg>
  <svg class="rule-dotted" style="top:415px" viewBox="0 0 330 8"><line x1="4" y1="4" x2="326" y2="4" stroke="#cfae63" stroke-width="1.5"/><circle cx="4" cy="4" r="3" fill="#cfae63"/><circle cx="326" cy="4" r="3" fill="#cfae63"/></svg>
  <svg class="rule-dotted" style="top:447px" viewBox="0 0 330 8"><line x1="4" y1="4" x2="326" y2="4" stroke="#cfae63" stroke-width="1.5"/><circle cx="4" cy="4" r="3" fill="#cfae63"/><circle cx="326" cy="4" r="3" fill="#cfae63"/></svg>
  <svg class="rule-dotted" style="top:478px" viewBox="0 0 330 8"><line x1="4" y1="4" x2="326" y2="4" stroke="#cfae63" stroke-width="1.5"/><circle cx="4" cy="4" r="3" fill="#cfae63"/><circle cx="326" cy="4" r="3" fill="#cfae63"/></svg>

  <ul class="service-list">
    <li class="centered service" style="top:361px">GARDEN MAINTENANCE</li>
    <li class="centered service" style="top:393px">HORTICULTURE</li>
    <li class="centered service" style="top:424px">LANDSCAPING</li>
    <li class="centered service" style="top:455px">DESIGN</li>
  </ul>

  <p class="centered offer">CALL US NOW FOR<br>YOUR FREE QUOTE</p>
  <p class="centered bonus">PRESENT THIS FLYER FOR YOUR FIRST HOUR FREE</p>
</section>

</body>
</html>
```